The 5 stages of grief experience

I'm an artist and I'm launching my art debut and i need a whole set of thing. I have the logo and the colors and the list of what I need:
Sponsorship proposal (I have the info to be pasted once design is ready)
Flyer for my art. It's about the 5 stages of grief and its like you go into a maze to go through each art instillation that takes you over each feeling, there is a lot of feelings and symmetry in the art.
Denial
Anger
Depression
Bargaining
Acceptance
Updates

We are rushing on this project if anyone is interested we need it asap Added Monday, March 6, 2017

Target Market(s)

Visual Art society

Font styles to use
Sans Serif

Colors
fee4d6
f8ba93
000000
5c5c5c
fbfbfb

Requirements
Must have
• Symmetry
• Feeling
• Strong message
• Bold
• An artistic idea I like a lot is a black and white moon changes and it's 5 different moons starting from a crescent ending in a full moon all next to each other or on top of each other and the phases underneath in small geometric font
Nice to have
• Softness
Should not have
• Femininity

```html
<!DOCTYPE html>
<html lang="en">
<head>
<meta charset="utf-8">
<title>Stages of Grief — Art Debut Flyer</title>
<link rel="stylesheet" href="https://fonts.googleapis.com/css2?family=Saira+Stencil+One&family=Bungee&family=Montserrat:wght@300&display=swap">
<style>
  :root {
    --slate-deep: #1f2227;
    --slate: #2d3037;
    --slate-light: #3a3e46;
    --white: #fbfbfb;
    --blush: #fee4d6;
    --peach: #f8ba93;
    --grey: #5c5c5c;
    --moon-tone: #9a9a9a;
  }
  html, body {
    margin: 0;
    padding: 0;
    overflow: hidden;
    background: #000000;
  }
  .flyer {
    position: relative;
    width: 1200px;
    height: 927px;
    overflow: hidden;
    background:
      radial-gradient(ellipse at 30% 20%, var(--slate-light) 0%, transparent 60%),
      radial-gradient(ellipse at 80% 80%, var(--slate-light) 0%, transparent 55%),
      linear-gradient(160deg, var(--slate) 0%, var(--slate-deep) 100%);
  }
  .flyer__title {
    position: absolute;
    top: 62px;
    left: 20px;
    width: 1160px;
    margin: 0;
    font-family: "Saira Stencil One", sans-serif;
    font-weight: 400;
    font-size: 120px;
    line-height: 1;
    letter-spacing: 6px;
    text-align: center;
    white-space: nowrap;
    background: linear-gradient(90deg, var(--white) 0%, var(--blush) 50%, var(--peach) 100%);
    -webkit-background-clip: text;
    background-clip: text;
    color: transparent;
  }
  .moon-phases {
    position: absolute;
    top: 215px;
    left: 40px;
    width: 1120px;
    height: 230px;
    border-radius: 115px;
    background: radial-gradient(ellipse at center, rgba(154,154,154,0.55) 0%, rgba(154,154,154,0.28) 55%, rgba(154,154,154,0.08) 100%);
  }
  .stages {
    position: absolute;
    left: 44px;
    top: 477px;
    margin: 0;
    padding: 0;
    list-style: none;
    font-family: "Bungee", sans-serif;
    font-size: 66px;
    line-height: 83px;
    letter-spacing: 1px;
    white-space: nowrap;
  }
  .stages__item:nth-child(1) { color: var(--white); }
  .stages__item:nth-child(2) { color: #fdf1ea; }
  .stages__item:nth-child(3) { color: var(--blush); }
  .stages__item:nth-child(4) { color: #fbcfb4; }
  .stages__item:nth-child(5) { color: var(--peach); }
  .host {
    position: absolute;
    left: 920px;
    top: 553px;
    width: 260px;
    text-align: center;
    font-family: "Montserrat", sans-serif;
    font-weight: 300;
    color: var(--grey);
  }
  .host__mark {
    display: block;
    width: 236px;
    height: 236px;
    margin: 0 auto 14px;
    border-radius: 50%;
    background: var(--grey);
  }
  .host__name {
    display: block;
    font-size: 48px;
    line-height: 1;
    letter-spacing: 10px;
    padding-left: 10px;
  }
  .host__tagline {
    display: block;
    font-size: 34px;
    line-height: 1.2;
    letter-spacing: 1px;
    white-space: nowrap;
  }
</style>
</head>
<body>
<main class="flyer">
  <h1 class="flyer__title">STAGES OF GRIEF</h1>

  <div class="moon-phases" role="img" aria-label="Photographs of five black and white moon phases in a row, from crescent through gibbous to full moon, then half and crescent"></div>

  <ul class="stages">
    <li class="stages__item">Denial</li>
    <li class="stages__item">Anger</li>
    <li class="stages__item">Depression</li>
    <li class="stages__item">Bargaining</li>
    <li class="stages__item">Acceptance</li>
  </ul>

  <div class="host">
    <span class="host__mark"></span>
    <span class="host__name">ECHO</span>
    <span class="host__tagline">ARTS EVENT</span>
  </div>
</main>
</body>
</html>
```